Need Business Card Design, Letterhead and a Basic Form layout based on Existing Logo

We need (1) a business card design, (2) a letterhead design and (3) a basic form layout for an international holding company. This holding company has just formed two (2) sub-companies. The logo is the same for each company with only a simple word change for each company. The business card, letterhead and form design will be essentially the same for each company... with only the one word change being different.
The names of the companies are as follows:
1. Kestrel Trust Services
2. Kestrel Immigration Services
The design for the business card, letterhead and Form must be strong, clean and classy.
Our clients will be older, wealthy and mostly Asian. The design must project strength, stability and confidence.
The card may contain the following data:
1. The Logo
2. The name of the person
3. The title of the person
4. The address of the company
5. The Company Phone number
6. The personal mobile number
7. The Skype number (VOIP)
8. The WICKR number (IM)
9. The email
10. The website
We will attach AI files of our logo for the "Kestrel Trust Services" company in the colors Black/White and Blue in both Horizontal and Vertical format... We have also included separate files of the logo icon.
We uploaded the AI files to give the designer the maximum options regarding color and effects. We included the separate files for the icon because we would like to give the designer the option of a watermark. Also, we think it might be nice to highlight the icon on the back of the card perhaps with the website address.
We are not sure which colors or color combinations would be best for these two companies. We know the colors must again project strength, stability and confidence. Perhaps, a combination that might include Tan, Black and White... not sure... need design help... remember this has to have the presence of a bank-like institution... no cartoonish designs or flashy color combinations... please.
The basic form layout will be used for various questionaires, input sheets and instructions.... etc.
NOTE: The fonts used in the logo are Trajan Pro Bold for word "KESTREL" and Trajan Pro Regular for "XXXXXXXXX SERVICES".

```html
<!DOCTYPE html>
<html lang="en">
<head>
<meta charset="utf-8">
<title>Kestrel Trust Services – Business Card</title>
<link rel="stylesheet" href="https://fonts.googleapis.com/css2?family=Cinzel:wght@400;600&family=Open+Sans:wght@400;600;700&display=swap">
<style>
  :root {
    --bg-light: #f4f4f4;
    --bg-mid: #d9d9d9;
    --ink: #111111;
    --card-black: #161616;
    --card-black-soft: #2a2a2a;
    --band-grey: #d4d4d4;
    --paper: #ffffff;
    --muted: #8a8a8a;
    --text-light: #e8e8e8;
  }
  * { margin: 0; padding: 0; box-sizing: border-box; }
  html, body { width: 1200px; height: 900px; overflow: hidden; }
  body {
    background: radial-gradient(ellipse at center, var(--bg-light) 0%, var(--bg-mid) 100%);
    font-family: "Open Sans", Arial, sans-serif;
    position: relative;
  }
  .card {
    position: absolute;
    left: 285px;
    width: 630px;
    height: 360px;
    overflow: hidden;
    box-shadow: 0 10px 28px rgba(0,0,0,0.28);
  }

  /* Back of card */
  .card-back {
    top: 60px;
    background: linear-gradient(135deg, var(--card-black-soft) 0%, var(--card-black) 55%, #0b0b0b 100%);
    color: var(--text-light);
    text-align: center;
  }
  .back-brand {
    position: absolute;
    top: 92px;
    left: 0; right: 0;
    display: flex;
    align-items: center;
    justify-content: center;
    gap: 18px;
  }
  .brand-square {
    width: 34px; height: 34px;
    background: var(--paper);
  }
  .back-brand .brand-name {
    font-family: "Cinzel", "Times New Roman", serif;
    font-weight: 600;
    font-size: 38px;
    letter-spacing: 3px;
    color: var(--paper);
  }
  .back-tagline {
    position: absolute;
    top: 210px; left: 0; right: 0;
    font-size: 13px;
    line-height: 19px;
    letter-spacing: 0.3px;
  }
  .back-web {
    position: absolute;
    top: 262px; left: 0; right: 0;
    font-family: "Cinzel", "Times New Roman", serif;
    font-size: 15px;
    letter-spacing: 2.5px;
  }

  /* Front of card */
  .card-front {
    top: 480px;
    background: var(--paper);
  }
  .front-shapes { position: absolute; inset: 0; }
  .front-brand {
    position: absolute;
    top: 62px; left: 44px;
    display: flex;
    align-items: center;
    gap: 20px;
  }
  .front-brand .brand-square {
    width: 56px; height: 56px;
    background: var(--ink);
  }
  .brand-lockup {
    font-family: "Cinzel", "Times New Roman", serif;
    font-weight: 400;
    color: var(--ink);
  }
  .brand-lockup .word-main {
    display: block;
    font-size: 36px;
    letter-spacing: 2px;
    line-height: 38px;
  }
  .brand-lockup .word-sub {
    display: block;
    font-size: 16px;
    letter-spacing: 1.5px;
    padding-left: 2px;
  }
  .person {
    position: absolute;
    top: 178px; left: 28px;
    font-size: 19px;
    color: var(--ink);
  }
  .person .person-name { font-weight: 700; }
  .person .person-title { font-size: 14px; font-weight: 600; }
  .person .divider { margin: 0 6px; font-weight: 400; }

  .contact-list {
    position: absolute;
    list-style: none;
    color: var(--text-light);
  }
  .contact-list li {
    display: flex;
    align-items: center;
    gap: 8px;
    font-size: 15px;
    line-height: 21px;
  }
  .contact-list svg { flex: none; }
  .contact-online { top: 120px; left: 398px; }
  .contact-online li { font-size: 14px; line-height: 20px; }
  .contact-phones { top: 226px; left: 28px; }
  .contact-phones li { font-size: 17px; line-height: 22px; }

  .office-address {
    position: absolute;
    top: 300px; left: 28px; right: 20px;
    font-size: 13px;
    line-height: 18px;
    color: var(--muted);
  }
</style>
</head>
<body>

  <section class="card card-back" aria-label="Business card, back">
    <div class="back-brand">
      <span class="brand-square" aria-hidden="true"></span>
      <span class="brand-name">KESTREL</span>
    </div>
    <p class="back-tagline">
      International Corporate Structuring, Asset Protection &amp; Estate Planning<br>
      Hong Kong | Guatemala | Nevis | Belize | Panama
    </p>
    <p class="back-web">WWW.KESTRELTRUST.COM</p>
  </section>

  <section class="card card-front" aria-label="Business card, front">
    <svg class="front-shapes" width="630" height="360" viewBox="0 0 630 360" aria-hidden="true">
      <rect x="0" y="170" width="630" height="35" fill="var(--band-grey)"/>
      <polygon points="0,205 330,205 420,108 630,108 630,360 0,360" fill="var(--card-black)"/>
    </svg>

    <div class="front-brand">
      <span class="brand-square" aria-hidden="true"></span>
      <div class="brand-lockup">
        <span class="word-main">KESTREL</span>
        <span class="word-sub">Trust Services</span>
      </div>
    </div>

    <p class="person">
      <span class="person-name">Marco Ellison</span><span class="divider">|</span><span class="person-title">Managing Director</span>
    </p>

    <ul class="contact-list contact-online">
      <li>
        <svg width="14" height="14" viewBox="0 0 14 14" aria-hidden="true"><rect width="14" height="14" rx="2" fill="var(--text-light)"/></svg>
        kestreldirect
      </li>
      <li>
        <svg width="14" height="14" viewBox="0 0 14 14" aria-hidden="true"><rect width="14" height="14" rx="2" fill="var(--text-light)"/><path d="M2 4 L7 8 L12 4 M2 4 H12 V11 H2 Z" fill="none" stroke="var(--card-black)" stroke-width="1.2"/></svg>
        marco@kestreltrust.com
      </li>
      <li>
        <svg width="14" height="14" viewBox="0 0 14 14" aria-hidden="true"><rect width="14" height="14" rx="2" fill="var(--text-light)"/><circle cx="7" cy="7" r="4.5" fill="none" stroke="var(--card-black)" stroke-width="1.1"/><path d="M2.5 7 H11.5 M7 2.5 V11.5" stroke="var(--card-black)" stroke-width="1"/></svg>
        www.kestreltrust.com
      </li>
    </ul>

    <ul class="contact-list contact-phones">
      <li>
        <svg width="14" height="14" viewBox="0 0 14 14" aria-hidden="true"><rect width="14" height="14" rx="2" fill="var(--text-light)"/><rect x="4.5" y="2" width="5" height="10" rx="1" fill="none" stroke="var(--card-black)" stroke-width="1.2"/></svg>
        502-3180-4472
      </li>
      <li>
        <svg width="14" height="14" viewBox="0 0 14 14" aria-hidden="true"><rect width="14" height="14" rx="2" fill="var(--text-light)"/><path d="M3.5 3 L5.5 3 L6.3 5.3 L5.2 6.3 Q6.2 8.3 7.8 8.9 L8.8 7.8 L11 8.6 L11 10.6 Q6.5 11 3.5 5.3 Z" fill="var(--card-black)"/></svg>
        502-3180-4472 (Local)
      </li>
      <li>
        <svg width="14" height="14" viewBox="0 0 14 14" aria-hidden="true"><rect width="14" height="14" rx="2" fill="var(--text-light)"/><path d="M3.5 3 L5.5 3 L6.3 5.3 L5.2 6.3 Q6.2 8.3 7.8 8.9 L8.8 7.8 L11 8.6 L11 10.6 Q6.5 11 3.5 5.3 Z" fill="var(--card-black)"/></svg>
        502-3180-4472 (International)
      </li>
    </ul>

    <p class="office-address">
      Local Office: Centro Empresarial Las Palmas, Office No. 10<br>
      Esquina Calle del Olvido y Callejón Real | Antigua, Guatemala
    </p>
  </section>

</body>
</html>
```